Kiswa Design

We need a flyer design for a product that we are a selling, a sacred Islamic cloth called a Kiswah, which is draped around the holy Kaaba in mecca every year.

The details we would like on the flyer are as follows:

Rare Kiswah of the holy Kaaba for sale (fitted in 1977 and 1982 vintage). For sale:

1) whole piece 15 meters x 2.60 meters : £60,000
2) 8 meters x 2.60 meters : £31,200
3) 4 meters x 2.60 meters : £15,600
4) 1 meter : £1500

(insert a high quality picture of holy Kaaba here, then underneath the picture, write the following:) "The Kaaba is covered by an expensive black cloth which is known as 'Kiswah' which is produced and changed every year"

(insert picture of our product here,i.e. use the document named MAIN IMAGE then underneath this picture write the following:) "Silk lampas weave Kiswah, woven silk on a black satin ground with Quranic calligraphy, the zig-zag bands of inscription alternate with the Shahadah and the inscription, 'God, exalted be His Glory!"

insert another picture of kiswah which i provided anywhere you like

(somewhere on flyer write the following) please note a percentage of sales will go towards Sadaqah for our Muslim brothers and sisters in need around the world

(somewhere on flyer write the following) Hallorand's international auction house authenticity document also available to prove the Kiswah is genuine.

100% genuine

contact us today! deals this good don't last forever.

email: relicoffer@tarnwickmail.com

Please use the images that I have attached on the flyer accordingly. Also feel free to be as creative as possible I want it to attract a lot of attention but also look professional so you may add some things to improve the look of the flyer.

note: the product being sold is on the pictures I've provided, in particular, i want file 2 "main image" in a large size on the flyer!

thank you! and happy holidays

Muslims and Islamic collectors

House

• the dimensions of the flyer is :
• A5 horizontal or vertical
• (210 x 148 mm)
• must have colors! up to you what colors to choose!

```html
<!DOCTYPE html>
<html lang="en">
<head>
<meta charset="utf-8">
<title>Rare Kiswah of the Holy Kaa'ba – For Sale</title>
<link rel="stylesheet" href="https://fonts.googleapis.com/css2?family=Anton&family=Arimo:ital,wght@0,400;0,700;1,700&display=swap">
<style>
  :root {
    --red: #e31b1b;
    --yellow: #ffe81a;
    --green: #22c93a;
    --green-light: #c9f27a;
    --ink: #111;
    --white: #fff;
    --cloth-dark: #1c1c1c;
    --cloth-grey: #6e6e6a;
  }
  * { box-sizing: border-box; margin: 0; padding: 0; }
  html, body { width: 847px; height: 1200px; overflow: hidden; background: var(--white); }
  .flyer {
    position: relative;
    width: 847px; height: 1200px;
    background: radial-gradient(ellipse at 60% 45%, #f4fbd0 0%, var(--green-light) 35%, var(--green) 85%);
    border: 6px solid var(--red);
    font-family: "Arimo", Arial, sans-serif;
    color: var(--ink);
    overflow: hidden;
  }
  .banner {
    position: absolute; left: 66px; top: 10px; width: 710px; height: 128px;
    background: var(--red);
    display: flex; align-items: center; justify-content: center;
  }
  .banner h2 {
    font-family: "Anton", Impact, sans-serif; font-weight: 400;
    font-size: 104px; letter-spacing: 6px; color: var(--yellow); line-height: 1;
  }
  .title { position: absolute; left: 0; right: 0; top: 158px; text-align: center; font-weight: 400; }
  .title .lead {
    font-family: "Anton", Impact, sans-serif; font-size: 48px; color: var(--red);
    text-shadow: 2px 2px 0 rgba(0,0,0,.35); line-height: 1.1; display: block;
  }
  .title .main {
    font-family: "Anton", Impact, sans-serif; font-size: 92px; color: var(--red);
    text-shadow: 3px 3px 0 rgba(0,0,0,.4); line-height: 1.05; display: block;
  }
  .title .sub { font-family: "Arimo", Arial, sans-serif; font-weight: 700; font-size: 28px; display: block; }
  .photo { position: absolute; left: 28px; width: 392px; }
  .photo-kaaba { top: 380px; height: 186px; background: linear-gradient(180deg, #bcb7ad 0%, #8c8578 40%, var(--cloth-dark) 60%, #9a9284 100%); }
  .photo-cloth { top: 644px; height: 330px; background: radial-gradient(ellipse at 50% 50%, #8a8a85 0%, var(--cloth-grey) 50%, #3d3d3a 100%); }
  .caption { position: absolute; left: 28px; width: 400px; font-weight: 700; font-size: 16.5px; line-height: 1.3; }
  .caption-kaaba { top: 572px; }
  .caption-cloth { top: 980px; }
  .genuine {
    position: absolute; left: 436px; top: 390px; width: 390px;
    font-family: "Anton", Impact, sans-serif; text-align: center; color: var(--white);
    text-shadow: 3px 3px 0 #333, -1px -1px 0 #333, 1px -1px 0 #333, -1px 1px 0 #333;
    line-height: 1;
  }
  .genuine .pct { font-size: 48px; display: block; }
  .genuine .word { font-size: 44px; display: block; letter-spacing: 2px; margin-top: 2px; }
  .prices { position: absolute; left: 436px; top: 496px; width: 395px; font-weight: 700; font-size: 20px; line-height: 34px; }
  .prices h3 { font-size: 20px; }
  .prices .gap { margin-top: 6px; }
  .certificate {
    position: absolute; left: 430px; top: 714px; width: 397px; height: 62px;
    background: var(--red); color: var(--white);
    font-weight: 700; font-size: 15px; line-height: 1.22; text-align: center;
    display: flex; align-items: center; justify-content: center; padding: 4px 10px;
  }
  .charity { position: absolute; left: 432px; top: 784px; width: 395px; font-style: italic; font-weight: 700; font-size: 15px; line-height: 1.25; }
  .deals { position: absolute; left: 430px; top: 834px; width: 397px; text-align: center; font-family: "Anton", Impact, sans-serif; color: var(--red); font-size: 38px; line-height: 1.05; }
  .contact { position: absolute; left: 430px; top: 916px; width: 400px; text-align: center; font-family: "Anton", Impact, sans-serif; font-size: 44px; line-height: 1.1; }
  .footer {
    position: absolute; left: 0; right: 0; top: 1118px; height: 66px;
    background: var(--red); display: flex; align-items: center; justify-content: center;
  }
  .footer a { color: var(--white); font-weight: 700; font-size: 46px; text-decoration: none; letter-spacing: 1px; }
</style>
</head>
<body>
<main class="flyer">
  <header>
    <div class="banner"><h2>FOR SALE</h2></div>
    <h1 class="title">
      <span class="lead">Rare Kiswah of the</span>
      <span class="main">Holy Kaa'ba</span>
      <span class="sub">Fitted in 1977 and 1982 Vintage</span>
    </h1>
  </header>

  <div class="photo photo-kaaba" role="img" aria-label="Photograph of the Holy Kaaba draped in its black Kiswah, surrounded by pilgrims"></div>
  <p class="caption caption-kaaba">The Kaa'ba is covered by an expensive black cloth known as 'kiswah' which is produced and changed every year.</p>

  <div class="photo photo-cloth" role="img" aria-label="Close view of the black silk Kiswah woven with Quranic calligraphy"></div>
  <p class="caption caption-cloth">Silk lampas weave Kiswah, woven silk on a blacksatin ground with Quranic calligraphy, the zig-zag bands of inscription alternate with the Shahadah and the inscription, 'God, exalted be His Glory!'</p>

  <p class="genuine"><span class="pct">100%</span><span class="word">GENUINE</span></p>
  <div class="prices">
    <h3>WHOLE PIECE</h3>
    <p>15 meters x 2.60 meters: &nbsp;£60,000</p>
    <h3 class="gap">RETAIL PIECES</h3>
    <p>8 meters x 2.60 meters: £31,200</p>
    <p>4 meters x 2.60 meters: £15,600</p>
    <p>1 meter: £1,500</p>
  </div>

  <p class="certificate">Hallorand's international auction house authenticity document also available to prove the Kiswa is genuine.</p>
  <p class="charity">A percentage of sales will go towards Sadaqah for our Muslim brothers and sisters in need around the world.</p>
  <p class="deals">Deals this good<br>don't last forever!</p>
  <p class="contact">Contact us today!</p>

  <footer class="footer"><a href="mailto:relicoffer@tarnwickmail.com">relicoffer@tarnwickmail.com</a></footer>
</main>
</body>
</html>
```